The Maplewood Family Clinic needs a Letterhead

We are a bilingual pediatric clinic located in Montreal, Canada.

Our english name is Maplewood Family Clinic
Our french name is Clinique du parc Verdelle

We offer complete care for children including general pediatric care, pediatric specialist care such as Ear, Nose and Throat, Urology, Neurology and Adolescent Medicine. We also have paramedical specialists such as psychologists, social workers, occupational therapists, speech and language pathologists.

The letterhead must use and be harmonious with our new logo. See Design #7150846. We need two types of letterhead. One for a the Logo and both english and french names on the top and the second with the list of current staff on the left. I have uploaded two old examples for you to see. Thanks and good luck.

Industry/Entity Type

Clinic

Font styles to use
Sans Serif

Colors
3176b5
9d9d9d

Requirements
Must have
• Include our logo.
Nice to have
• Most of our printing is done in black and white. So a grayscale design is fine.
I have included a color and grayscale versions of our logo.

We prefer clean modern designs.

```html
<!DOCTYPE html>
<html lang="en">
<head>
<meta charset="utf-8">
<title>Maplewood Family Clinic – Letterhead</title>
<link rel="stylesheet" href="https://fonts.googleapis.com/css2?family=Saira+Semi+Condensed:wght@500&family=Noto+Sans:wght@400;700&display=swap">
<style>
  :root {
    --backdrop: #d9d9d9;
    --page-dark: #2b2b2b;
    --page-light: #ffffff;
    --ink-grey: #9d9d9d;
    --ink-label: #8c8c8c;
    --ink-name: #7a7a7a;
  }
  html, body {
    margin: 0;
    width: 1200px;
    height: 900px;
    overflow: hidden;
    background: var(--backdrop);
  }
  .letterhead {
    position: absolute;
    left: 305px;
    top: 12px;
    width: 592px;
    height: 875px;
    background: var(--page-dark);
    overflow: hidden;
  }
  .letterhead__sheet {
    position: absolute;
    inset: 0;
  }
  .brand {
    position: absolute;
    left: 30px;
    top: 24px;
    display: flex;
    align-items: center;
    gap: 8px;
    font-family: "Saira Semi Condensed", sans-serif;
    font-weight: 500;
    font-size: 14px;
    line-height: 15px;
    color: var(--ink-grey);
  }
  .brand__dot {
    width: 30px;
    height: 30px;
    border-radius: 50%;
    background: var(--ink-grey);
  }
  .masthead {
    position: absolute;
    right: 34px;
    top: 14px;
    text-align: right;
    font-family: "Saira Semi Condensed", sans-serif;
    font-weight: 500;
    color: var(--ink-grey);
  }
  .masthead__en { font-size: 25px; line-height: 30px; margin: 0; }
  .masthead__fr { font-size: 20px; line-height: 24px; margin: 0; }
  .staff {
    position: absolute;
    left: 423px;
    top: 103px;
    width: 165px;
    font-family: "Noto Sans", sans-serif;
    font-size: 7.5px;
    line-height: 9.7px;
    color: var(--ink-name);
  }
  .staff__group { margin: 0 0 11px; }
  .staff__group--wide { margin-bottom: 17px; }
  .staff__label {
    display: block;
    font-weight: 700;
    font-size: 8.6px;
    line-height: 11px;
    color: var(--ink-label);
  }
  .footer {
    position: absolute;
    left: 0;
    right: 0;
    top: 811px;
    text-align: center;
    font-family: "Saira Semi Condensed", sans-serif;
    font-weight: 500;
    font-size: 21px;
    line-height: 25px;
    color: var(--ink-grey);
  }
  .footer p { margin: 0; }
</style>
</head>
<body>
<main class="letterhead">
  <svg class="letterhead__sheet" width="592" height="875" viewBox="0 0 592 875" aria-hidden="true">
    <path fill="var(--page-light)" d="M0,203 Q190,115 390,83 Q406,81 406,98 L406,503 Q406,518 421,518 L576,518 Q592,518 592,506 L592,723 Q320,790 0,793 Z"/>
  </svg>

  <div class="brand">
    <span class="brand__dot"></span>
    <span>Maplewood<br>Family Clinic</span>
  </div>

  <header class="masthead">
    <h1 class="masthead__en">Maplewood Family Clinic</h1>
    <p class="masthead__fr">Clinique du parc Verdelle</p>
  </header>

  <aside class="staff">
    <p class="staff__group staff__group--wide"><span class="staff__label">Addresse / Address</span>2280 boul. Verdelle<br>Suite 210<br>Verdelle, Qc<br>H4R 2K8<br>Tél. (514) 555-0142<br>Fax. (514) 555-0187</p>
    <p class="staff__group staff__group--wide"><span class="staff__label">Pédiatres / Pediatricians</span>H. Laurier<br>J. Morel<br>R. Beaulieu<br>D. Tremblay<br>N. Gagnon<br>M. Fortin<br>D. Roy</p>
    <p class="staff__group"><span class="staff__label">Neurologue / Neurologist</span>M. Caron</p>
    <p class="staff__group"><span class="staff__label">O.R.L. / E.N.T.</span>T. Lavoie</p>
    <p class="staff__group"><span class="staff__label">Urologue / Urologist</span>R. Pelletier</p>
    <p class="staff__group"><span class="staff__label">Psychologues / Psychologists</span>H. Bouchard<br>A. Girard</p>
    <p class="staff__group"><span class="staff__label">Travailleuse social / Social worker</span>S. Dubois</p>
    <p class="staff__group"><span class="staff__label">Dietetiste / Dietician</span>L. Côté</p>
    <p class="staff__group"><span class="staff__label">Gerante / Manager</span>C. Bergeron</p>
  </aside>

  <footer class="footer">
    <p>2280 boul. Verdelle, Suite 210 Verdelle, Qc, H4R2K8</p>
    <p>Tel (514) 555-0142 Fax (514) 555-0187</p>
  </footer>
</main>
</body>
</html>
```